Brightmoor Games Company Wordpress Site

We need a new company site for an established game development studio in Dallas, Texas. It should be a much more professional look than we have now, but we still want it to be a bit fun. It needs to be built so we can add more content later (as we publish new games, gain new clients, etc).
This could be built as a single page, multi-page, or a hybrid design. The design must scale to fit desktop and mobile browsers. This job will require that the website be both designed, and coded in Wordpress.
Your design should include at least the following areas:
MAIN LANDING AREA
- The company logo.
- Basic company info with a call to action.
- Twitter feed integration for news.
- Social media links.
GAMES AREA
- Section for games we have developed (logos and links).
- Second section for games we have ported (logos and links).
- This area should be designed to expand to many games.
SERVICES AREA
- Two or three paragraphs of text.
- A few images related to our services.
- FAQ about our services.
CONTACT AREA
- One or two paragraphs of text.
- Contact form.
ABOUT AREA
- Two or three paragraphs about the company.
- A few images about the company.
We will provide the final text and images to use on the site once a winning design is selected.
Again we need a more professional, modern, and more minimalist look than our current site (www.brightmoorgames-example.com), but are not opposed to something fun. We want to retain our current logo (included in the download). We know the name of the company is offbeat, but please avoid anything gross, dark, or violent, as professionalism is key. Leaning on our past projects is a good idea because we’ve worked with some very reputable game developers.
Hey everyone. We've received some fantastic submissions and want to continue working with a few of them for a little more time before making our decision. So we have extended the deadline and have also added 2nd and 3rd place rewards. Thanks to everybody who submitted!
Target Market(s)
Gamers, game professionals, developers, technology leaders, etc.
Industry/Entity Type
Games
Coding
Coded - Design and coding required
Look and feel

```html
<!DOCTYPE html>
<html lang="en">
<head>
<meta charset="utf-8">
<title>Brightmoor Games</title>
<link href="https://fonts.googleapis.com/css2?family=Josefin+Sans:wght@300;400&family=Jost:wght@400;500;600&family=Oswald:wght@300&display=swap" rel="stylesheet">
<style>
:root{
  --bg-dark:#1c1a1c;
  --bg-mid:#262325;
  --bg-deep:#141214;
  --bg-strip:#161416;
  --text:#ffffff;
  --muted:#8d8a8c;
  --soft:#b9b6b8;
  --accent:#2f7fd0;
  --accent-line:#2b6fb5;
  --ring:#5a5659;
  --field:#3b383a;
}
*{margin:0;padding:0;box-sizing:border-box}
html,body{width:1200px;height:2703px;overflow:hidden;background:var(--bg-dark)}
body{position:relative;font-family:"Jost",sans-serif;color:var(--text)}
.display{font-family:"Josefin Sans",sans-serif;font-weight:300;font-variant:small-caps;letter-spacing:4px;text-transform:none}
section,header,footer{position:absolute;left:0;width:1200px}
.abs{position:absolute}

/* hero */
.hero{top:0;height:520px;overflow:hidden}
.hero-art{position:absolute;inset:0;background:radial-gradient(ellipse at 50% 92%,#d88a2c 0%,#8a4a1c 18%,#4a2a1c 45%,#2a1a18 75%,#1a1214 100%)}
.brand{left:135px;top:70px;display:flex;align-items:center;gap:10px;font-size:26px;font-weight:600;letter-spacing:1px;color:var(--text)}
.brand .dot{width:22px;height:22px;border-radius:50%;background:var(--text)}
.contact-top{top:40px;font-size:16px;font-weight:500}
.contact-top.phone{left:535px}
.contact-top.mail{left:752px;font-size:13px;font-weight:400;top:43px}
.socials{display:flex;gap:10px}
.socials span{width:12px;height:12px;border-radius:50%;border:1.5px solid currentColor;display:block}
.socials.top{left:948px;top:45px;color:#e8e6e7}
.nav{left:366px;top:121px;display:flex;gap:23px;font-size:11.5px;font-weight:600;letter-spacing:1px}
.nav a{color:var(--text);text-decoration:none}
.nav a.current{color:var(--accent)}
.btn-solid{background:var(--accent);color:var(--text);border-radius:20px;font-size:12px;font-weight:600;letter-spacing:1px;display:flex;align-items:center;justify-content:center}
.inquire{left:919px;top:112px;width:144px;height:32px}
.hero-title{left:0;width:1200px;top:240px;text-align:center;font-size:44px;line-height:48px}
.platforms{left:480px;top:357px;display:flex;gap:11px}
.platforms span{width:40px;height:40px;border-radius:50%;border:1.5px solid #e6e3e4;display:flex;align-items:center;justify-content:center}

/* game strip */
.games{top:520px;height:120px;background:linear-gradient(#1a1718,#141213)}
.game-name{top:46px;width:170px;margin-left:-85px;text-align:center;font-family:"Jost",sans-serif;font-weight:600;font-size:19px;color:#a9a6a8}
.game-name.active{color:#d9c23a}

/* services */
.services{top:640px;height:549px;background:var(--bg-mid)}
.section-title{left:0;width:1200px;text-align:center;font-size:34px;line-height:40px}
.service{width:300px;margin-left:-150px;text-align:center}
.service svg{display:block;margin:0 auto}
.service h3{margin-top:20px;font-size:16px;font-weight:500;line-height:24px;text-decoration:underline;text-underline-offset:4px}
.service p{margin-top:14px;font-size:12.5px;line-height:17px;color:var(--muted);padding:0 10px}
.btn-line{border:1.5px solid var(--accent-line);border-radius:20px;color:var(--accent);font-size:10px;font-weight:600;letter-spacing:1px;display:flex;align-items:center;justify-content:center}
.service .btn-line,.service .btn-solid{width:81px;height:31px;margin:30px auto 0;font-size:10px}

/* about */
.about{top:1189px;height:441px;background:var(--bg-deep)}
.about-photo{left:0;top:0;width:600px;height:441px;background:linear-gradient(120deg,#3a2a22 0%,#7a5a3a 35%,#3a2a22 60%,#0f0d0e 100%)}
.about-kicker{left:681px;top:77px;font-size:16px;font-weight:500}
.about-title{left:681px;top:124px;width:420px;font-size:34px;line-height:36px}
.about-text{left:681px;top:204px;width:430px;font-size:13px;line-height:19px;color:var(--muted)}
.about .btn-line{left:681px;top:329px;width:144px;height:31px}

/* why us */
.why{top:1630px;height:388px;background:var(--bg-mid)}
.stat{width:200px;margin-left:-100px;text-align:center;top:160px}
.stat .ring{width:120px;height:120px;margin:0 auto;border-radius:50%;border:1.5px solid var(--ring);display:flex;align-items:center;justify-content:center;font-family:"Oswald",sans-serif;font-weight:300;font-size:38px}
.stat .label{margin-top:24px;font-size:10px;font-weight:600;letter-spacing:1px}

/* tweet */
.tweet{top:2018px;height:159px;background:var(--bg-strip)}
.tweet-mark{left:281px;top:62px;width:40px;height:40px;border-radius:50%;background:var(--accent)}
.tweet-rule{left:360px;top:28px;width:1px;height:103px;background:#343133}
.tweet-text{left:391px;top:48px;width:520px;font-size:13px;line-height:18px;color:var(--soft)}
.tweet-text b{color:var(--accent);font-weight:500}
.tweet-date{left:391px;top:96px;font-size:9px;letter-spacing:1px;color:var(--soft)}
.pager{left:868px;top:122px;display:flex;gap:4px}
.pager span{width:7px;height:7px;border-radius:50%;border:1px solid var(--muted)}

/* contact */
.contact{top:2177px;height:526px;overflow:hidden}
.contact-art{position:absolute;inset:0;background:linear-gradient(#1e1b1d 0%,#262225 45%,#161315 100%)}
.contact .section-title{top:75px}
.contact-sub{left:0;width:1200px;top:117px;text-align:center;font-size:14px}
.field{height:31px;border:1px solid var(--field);background:rgba(20,18,20,.6);font-size:9px;letter-spacing:1px;color:var(--muted);padding:9px 10px}
.field.name{left:279px;top:169px;width:225px}
.field.email{left:519px;top:169px;width:225px}
.field.phone{left:759px;top:169px;width:161px}
.field.message{left:279px;top:216px;width:641px;height:95px}
.send{left:552px;top:344px;width:81px;height:31px;font-size:10px}
.foot-left{left:135px;top:453px;font-size:12px;color:var(--soft);line-height:18px}
.foot-left small{font-size:9px;color:var(--muted)}
.foot-mid{left:681px;top:453px;font-size:12px;color:var(--soft);line-height:18px}
.foot-mid small{font-size:9px;color:var(--muted)}
.socials.bottom{left:950px;top:463px;color:var(--soft)}
.socials.bottom span.on{color:var(--accent)}
</style>
</head>
<body>

<header class="hero">
  <div class="hero-art" role="img" aria-label="Warm painted fantasy scene of characters gathered around a campfire"></div>
  <div class="abs brand"><span class="dot"></span>Brightmoor</div>
  <div class="abs contact-top phone">Call. 1 (555) 014 2290</div>
  <div class="abs contact-top mail">e. game@example.com</div>
  <div class="abs socials top"><span></span><span></span><span></span><span></span></div>
  <nav class="abs nav">
    <a class="current" href="#">HOME</a><a href="#">COMPANY</a><a href="#">GAMES</a><a href="#">SERVICES</a><a href="#">NEWS</a><a href="#">FAQ'S</a><a href="#">CONTACT US</a>
  </nav>
  <div class="abs btn-solid inquire">INQUIRE NOW!</div>
  <h1 class="abs hero-title display">We Make<br>Awesome Games</h1>
  <div class="abs platforms">
    <span><svg width="14" height="14" viewBox="0 0 14 14"><path d="M4 2 L11 7 L4 12 Z" fill="none" stroke="#fff" stroke-width="1.4"/></svg></span>
    <span></span>
    <span></span>
    <span><svg width="16" height="14" viewBox="0 0 16 14"><path d="M2 12 C3 6 7 4 11 4 M9 1 L12 4 L9 7" fill="none" stroke="#fff" stroke-width="1.4"/></svg></span>
  </div>
</header>

<section class="games">
  <div class="abs game-name" style="left:121px">Valor Rising</div>
  <div class="abs game-name" style="left:315px">Dash Clash</div>
  <div class="abs game-name active" style="left:506px">Canopy Trek</div>
  <div class="abs game-name" style="left:699px">Ember Tactics</div>
  <div class="abs game-name" style="left:892px">Gem Journal</div>
  <div class="abs game-name" style="left:1081px">Lumen Tales</div>
</section>

<section class="services">
  <h2 class="abs section-title display" style="top:72px">Our Best Selling<br>Game Development Services</h2>
  <div class="abs service" style="left:279px;top:198px">
    <svg width="66" height="66" viewBox="0 0 66 66" fill="none" stroke="#2f7fd0" stroke-width="2"><path d="M33 14 L45 34 L33 54 L21 34 Z"/><circle cx="33" cy="34" r="4"/><path d="M4 12 H62"/><rect x="29" y="6" width="8" height="10"/><rect x="2" y="8" width="6" height="6"/><rect x="58" y="8" width="6" height="6"/><path d="M27 54 H39 V62 H27 Z"/></svg>
    <h3>Game Design with<br>Finest Layout</h3>
    <p>Sed ut perspiciatis unde omnis iste natus error sit voluptatem accusantium doloremque laudantium, totam rem aperiam, eaque ipsa ...</p>
    <div class="btn-line">MORE</div>
  </div>
  <div class="abs service" style="left:600px;top:198px">
    <svg width="66" height="66" viewBox="0 0 66 66" fill="none" stroke="#2f7fd0" stroke-width="2"><rect x="6" y="4" width="48" height="40"/><rect x="12" y="18" width="48" height="42"/><path d="M12 26 H60"/><path d="M28 36 L22 42 L28 48 M44 36 L50 42 L44 48 M39 34 L33 50"/></svg>
    <h3>Game Developer with<br>3D Modeling</h3>
    <p>Sed ut perspiciatis unde omnis iste natus error sit voluptatem accusantium doloremque laudantium, totam rem aperiam, eaque ipsa ...</p>
    <div class="btn-line">MORE</div>
  </div>
  <div class="abs service" style="left:919px;top:198px">
    <svg width="66" height="66" viewBox="0 0 66 66" fill="none" stroke="#2f7fd0" stroke-width="2"><rect x="4" y="18" width="58" height="42" rx="3"/><path d="M24 18 V10 H42 V18"/><path d="M4 32 H62"/><path d="M22 28 V50 M44 28 V50"/><circle cx="22" cy="26" r="3"/><circle cx="44" cy="26" r="3"/></svg>
    <h3>Contact Us For Some<br>Immediate Help</h3>
    <p>Sed ut perspiciatis unde omnis iste natus error sit voluptatem accusantium doloremque laudantium, totam rem aperiam, eaque ipsa ...</p>
    <div class="btn-solid">MORE</div>
  </div>
</section>

<section class="about">
  <div class="abs about-photo" role="img" aria-label="Photo of a small team working together around a laptop"></div>
  <div class="abs about-kicker">Brightmoor Games</div>
  <h2 class="abs about-title display">We Make Dreams Come To Life</h2>
  <p class="abs about-text">We are a dedicated team of developers, designers, artists, and most importantly gaming enthusiasts programmers. Lorem ipsum dolor sit amet, consectetur adipiscing elit. Fusce vitae ante pharetra, molestie nunc non, interdum ipsum.</p>
  <div class="abs btn-line">ABOUT US</div>
</section>

<section class="why">
  <h2 class="abs section-title display" style="top:92px">Why Us</h2>
  <div class="abs stat" style="left:240px"><div class="ring">135+</div><div class="label">GAMES DEVELOPED</div></div>
  <div class="abs stat" style="left:479px"><div class="ring">100+</div><div class="label">HAPPY CLIENTS</div></div>
  <div class="abs stat" style="left:719px"><div class="ring">50+</div><div class="label">SKILLED TEAM</div></div>
  <div class="abs stat" style="left:959px"><div class="ring">1000+</div><div class="label">CUP OF COFFEE</div></div>
</section>

<section class="tweet">
  <div class="abs tweet-mark"></div>
  <div class="abs tweet-rule"></div>
  <p class="abs tweet-text">RT <b>@HollowDeepGame</b>: Hey Console fans! Excited to announce you can pre-order Hollow Deep today on Console/Handheld (Cross Buy FTW!) for 10% off. And it's...</p>
  <div class="abs tweet-date">01:51:39 PM 07.24.2018</div>
  <div class="abs pager"><span></span><span></span><span></span><span></span><span></span></div>
</section>

<section class="contact">
  <div class="contact-art" role="img" aria-label="Dark misty forest backdrop"></div>
  <h2 class="abs section-title display">Contact Us</h2>
  <p class="abs contact-sub">We would love to hear from you. Lorem ipsum dolor sit amet,</p>
  <div class="abs field name">NAME</div>
  <div class="abs field email">EMAIL</div>
  <div class="abs field phone">PHONE</div>
  <div class="abs field message">TYPE YOUR MESSAGE</div>
  <div class="abs btn-solid send">SEND</div>
  <div class="abs foot-left">© 2018 Brightmoor Games, LLC. All Rights Reserved.<br><small>Terms and Privacy</small></div>
  <div class="abs foot-mid">Call Us. 1 (555) 014 2290<br><small>e. game@example.com</small></div>
  <div class="abs socials bottom"><span></span><span class="on"></span><span></span><span></span></div>
</section>

</body>
</html>
```